Harbor Sushi & Steak Dinner Menu

I'm looking for a MENU design with a particular feel. I want to have a base template made that I can then use for future alterations to the menu; ie I can go in and change out different entrees as the menu changes but the template will remain the same. (Ideally it would be in an Apple Pages format.). Also ideally - dinner menu will occupy 2 pages 8.5 x 11. The restaurant's name is Harbor. It is a MODERN steak house that will also feature Sushi, a Raw Bar, Exquisite Cocktails and a sophisticated nightlife crowd. I have attached our LOGO, a secondary logo that we will be featuring throughout the project including on the menu cover (the gold U). Finally - I have attached the content that we would like to see. AGAIN - I REITERATE: High end dining and lounge atmosphere. A couple of restaurants / menus that I love are Corvellin in NYC and Marrowby Steakhouse in Long Island NY. Please do not duplicate - just trying to offer some suggestions.

Requirements
Must have
• A sophisticated and elegant feel without being stuffy or old.

```html
<!DOCTYPE html>
<html lang="en">
<head>
<meta charset="utf-8">
<title>Harbor Sushi &amp; Steak — Dinner Menu</title>
<link rel="stylesheet" href="https://fonts.googleapis.com/css2?family=EB+Garamond:ital,wght@0,400;0,500;0,600;0,700;1,400&display=swap">
<style>
  :root {
    --backdrop: #2b2b2b;
    --paper: #f2f2f2;
    --slate: #1c1c1c;
    --slate-light: #2a2a2a;
    --gold: #e2bb5a;
    --gold-deep: #b8874a;
    --gold-pale: #e8c99a;
    --wine: #c4293b;
    --ink: #f3f0ea;
  }
  * { box-sizing: border-box; margin: 0; padding: 0; }
  html, body {
    width: 1200px; height: 900px; overflow: hidden;
    background: var(--backdrop);
    font-family: "EB Garamond", Georgia, serif;
  }
  .menu-set {
    display: flex; gap: 16px; justify-content: center; align-items: center;
    width: 1200px; height: 900px;
  }
  .sheet {
    width: 380px; height: 492px; background: var(--paper);
    padding: 14px; box-shadow: 0 6px 18px rgba(0,0,0,.35);
  }
  .panel {
    position: relative; width: 100%; height: 100%; overflow: hidden;
    background: radial-gradient(ellipse at 40% 30%, var(--slate-light), var(--slate) 75%);
    color: var(--ink);
  }
  .brand {
    text-align: center; color: var(--gold);
    font-weight: 500; letter-spacing: .18em;
  }
  .brand-mark {
    display: inline-block; width: .45em; height: .45em;
    background: var(--wine); margin-right: .35em; vertical-align: .15em;
  }
  .tab {
    position: absolute; width: 24px; height: 34px;
    background: linear-gradient(180deg, var(--gold-pale), var(--gold-deep));
  }

  /* Cover */
  .cover .brand { font-size: 40px; padding-top: 42px; }
  .cover-photo {
    width: 150px; height: 150px; border-radius: 50%;
    margin: 46px auto 0;
    background: radial-gradient(circle, #c86a34 0 18%, #5f8a3c 32%, #3f6b2f 55%, #f4f4f2 60% 100%);
  }
  .cover-title { margin: 34px auto 0; width: 200px; text-align: center; }
  .cover-title .rule { height: 1px; background: var(--gold); }
  .cover-title h1 {
    color: var(--gold); font-size: 36px; font-weight: 700;
    letter-spacing: .04em; line-height: 1.1; padding: 6px 0 4px;
  }
  .cover-tagline {
    color: var(--wine); font-size: 10px; text-align: center;
    letter-spacing: .04em; margin-top: 8px;
  }
  .cover .tab { left: 164px; bottom: 18px; }

  /* Inside pages */
  .inside .brand { font-size: 24px; padding-top: 20px; }
  .inside .tab { right: 12px; top: 10px; }
  .columns {
    display: grid; gap: 12px; padding: 14px 14px 0;
    font-size: 7px; line-height: 1.22;
  }
  .columns.even { grid-template-columns: 1fr 1fr; }
  .columns.wide-left { grid-template-columns: 1.25fr 1fr; }
  .section { margin-bottom: 7px; }
  .section h2 {
    color: var(--gold); font-size: 9px; font-weight: 700;
    letter-spacing: .03em; margin-bottom: 1px;
  }
  .item { margin-bottom: .5px; }
  .item b { font-weight: 600; }
  .item i { font-style: italic; opacity: .9; }
  .note { color: var(--gold); font-style: italic; }
</style>
</head>
<body>
<main class="menu-set">

  <!-- Cover -->
  <section class="sheet cover">
    <div class="panel">
      <div class="brand"><span class="brand-mark"></span>HARBOR</div>
      <div class="cover-photo" role="img" aria-label="Photo of seared salmon on a mixed green salad, plated on white"></div>
      <div class="cover-title">
        <div class="rule"></div>
        <h1>MENU</h1>
        <div class="rule"></div>
      </div>
      <p class="cover-tagline">RICH FOOD MENU FOR EVERY TASTE!</p>
      <div class="tab"></div>
    </div>
  </section>

  <!-- Inside left: sushi & raw bar -->
  <section class="sheet inside">
    <div class="panel">
      <div class="brand">HARBOR</div>
      <div class="tab"></div>
      <div class="columns even">
        <div>
          <div class="section">
            <h2>SUSHI / SASHIMI</h2>
            <p class="item"><b>Toro:</b> <i>blue fin tuna belly (gf)</i></p>
            <p class="item"><b>Unagi:</b> <i>fresh water eel (gf)</i></p>
            <p class="item"><b>Ebi:</b> <i>cooked shrimp (gf)</i></p>
            <p class="item"><b>Sake:</b> <i>salmon (gf)</i></p>
            <p class="item"><b>Hamachi:</b> <i>yellowtail (gf)</i></p>
            <p class="item"><b>Madai:</b> <i>red snapper (gf)</i></p>
            <p class="item"><b>Uni:</b> <i>sea urchin (gf)</i></p>
            <p class="item"><b>Maguro:</b> <i>tuna (gf)</i></p>
            <p class="item"><b>Hirame:</b> <i>fluke (gf)</i></p>
          </div>
          <div class="section">
            <h2>SUSHI PLATTERS</h2>
            <p class="item"><b>Small:</b> <i>Five Pieces assorted sushi, nine pieces sashimi, spicy tuna roll (gf)</i></p>
            <p class="item"><b>Large:</b> <i>Eight Pieces assorted sushi, eighteen pieces of sashimi, alaskan roll, rainbow roll (gf)</i></p>
          </div>
          <div class="section">
            <h2>CLASSIC ROLLS</h2>
            <p class="item"><b>Yellowtail:</b> <i>inside out roll with scallions (gf)</i></p>
            <p class="item"><b>Spicy Tuna or Salmon or Yellowtail:</b> <i>spicy mayo</i></p>
            <p class="item"><b>California:</b> <i>crab meat, cucumber and avocado (gf)</i></p>
            <p class="item"><b>Vegetable:</b> <i>avocado, cucumber, asparagus and pickled reddish (gf)</i></p>
            <p class="item"><b>Spider:</b> <i>soft shell crab and avocado with eel sauce</i></p>
            <p class="item"><b>Shrimp Tempura:</b> <i>deep fried tempura shrimp and eel sauce</i></p>
            <p class="item"><b>Alaskan:</b> <i>salmon and avocado (gf)</i></p>
          </div>
          <div class="section">
            <h2>SPECIAL ROLLS</h2>
            <p class="item"><b>The Harbor:</b> <i>tuna, salmon, yellowtail, avocado, cucumber, spicy mayo, soy bean paper</i></p>
            <p class="item"><b>King Crab Rainbow:</b> <i>king crab, avocado, cucumbers, assorted fish on top</i></p>
            <p class="item"><b>Empress:</b> <i>Shrimp tempura, spicy tuna on top, eel sauce, spicy mayo</i></p>
            <p class="item"><b>Spicy Girl:</b> <i>Spicy crunchy crab meat, cucumber, shrimp on top</i></p>
          </div>
        </div>
        <div>
          <div class="section">
            <p class="item"><b>Dragon:</b> <i>Eel, cucumber, avocado, and tobiko on top, eel sauce</i></p>
            <p class="item"><b>Yummy:</b> <i>spicy crunchy salmon, avocado, mango and salmon on top</i></p>
            <p class="item"><b>No. 9:</b> <i>Shrimp Tempura, avocado, kani, spicy mayo, tobiko</i></p>
            <p class="item"><b>Sunrise Roll:</b> <i>spicy crunchy tuna and avocado, spicy crunchy salmon on top</i></p>
          </div>
          <div class="section">
            <h2>SEAFOOD RAW BAR</h2>
            <p class="item">Lobster Cocktail</p>
            <p class="item">Shrimp Cocktail</p>
            <p class="item">Clams on the Half Shell</p>
            <p class="item">Oysters on the Half Shell</p>
            <p class="item">Colossal Crab Cocktail</p>
            <p class="item"><b>Raw Bar Plate for One:</b> <i>Two Shrimp, Half of a One Pound Lobster, Two Clams, One East Coast Oyster, One West Coast Oyster</i></p>
          </div>
          <div class="section">
            <h2>APPS</h2>
            <p class="item"><b>BAO Bun:</b> <i>hoisin bbq pancetta cut pork loin, crispy onions, micro mint</i></p>
            <p class="item"><b>Five Spice Crispy Popcorn Crusted Prawns (2):</b> <i>classic beurre blanc</i></p>
            <p class="item"><b>Jumbo Lump Crab:</b> <i>citrus miso drizzle, spring pea puree, micro greens</i></p>
            <p class="item"><b>Crispy Wonton Napoleon:</b> <i>cucumber gallete, ahi tuna, jumbo lump crab meat, wasabi aioli, shoestring wontons</i></p>
            <p class="item"><b>PEI Mussels:</b> <i>charred artichoke hearts, blistered heirloom tomatoes, garlic white wine broth</i></p>
            <p class="item"><b>New Zealand or Domestic Small Eye Lamb Chop (1):</b> <i>crispy porcini risotto cake</i></p>
          </div>
          <div class="section">
            <h2>SEAFOOD PLATTERS (gf)</h2>
            <p class="item">Shrimp, Oysters, Clams, Lobster and Crab</p>
            <p class="item note">Large or Colossal</p>
          </div>
        </div>
      </div>
    </div>
  </section>

  <!-- Inside right: salads, entrees, steaks -->
  <section class="sheet inside">
    <div class="panel">
      <div class="brand">HARBOR</div>
      <div class="tab"></div>
      <div class="columns wide-left">
        <div>
          <div class="section">
            <h2>SALADS</h2>
            <p class="item"><b>Classic Wedge:</b> <i>bleu cheese, bacon lardons, heirloom tomatoes</i></p>
            <p class="item"><b>Mixed Baby Greens:</b> <i>heirloom tomatoes, cucumber, red onion, dijon vinaigrette</i></p>
            <p class="item"><b>Tabouleh:</b> <i>buckwheat grain, fresh mint, tomato concasse, cucumber, parsley, fresh squeezed lemon, EVOO, salt and pepper</i></p>
            <p class="item"><b>Tomato Mozzarella Salad / Burratta</b></p>
            <p class="item"><b>Spinach Salad:</b> <i>green apple, feta, currants, with persimmons vinaigrette</i></p>
            <p class="item"><b>Kale Caesar:</b> <i>homemade cacio e'pepe dressing, pecorino and parmesan cheese, toasted croutons</i></p>
          </div>
          <div class="section">
            <h2>ENTREES</h2>
            <p class="item"><b>Pan Roasted Miso Glazed Black Cod:</b> <i>green tea noodle stir fry, Napa cabbage, carrot, Japanese eggplant</i></p>
            <p class="item"><b>Pan Seared Striped Bass:</b> <i>lobster succotash in a tomato saffron broth</i></p>
            <p class="item"><b>E.V.O.O. Salted / Grilled Swordfish:</b> <i>sun dried tomato, olive and caper tapenade, over basmati rice</i></p>
            <p class="item"><b>Grilled Half Chicken:</b> <i>sun dried tomato and basil israeli cous-cous, pan au jus</i></p>
            <p class="item"><b>Roasted Fresh Cavatelli Ratatouille:</b> <i>vegetable broth</i></p>
            <p class="item"><b>Lobster Cartoccio:</b> <i>shrimp, mussels, clams, fresh herb tomato broth, tossed with bucatini</i></p>
            <p class="item"><b>Charred Artichoke Hearts:</b> <i>heirloom tomatoes, caper berries, spring onions, fresh basil, white wine reduction over forbidden rice (gf)</i></p>
            <p class="item"><b>Mediterranean Grilled Veggie Plate:</b> <i>artichoke hearts, Japanese eggplant, green &amp; white asparagus, seared heirloom tomatoes, roasted baby carrots, cauliflower rice, evoo &amp; fig drizzle (gf)</i></p>
          </div>
        </div>
        <div>
          <div class="section">
            <h2>USDA PRIME STEAKS (gf)</h2>
            <p class="item">10 Oz Filet</p>
            <p class="item">14 or 16 oz New York Strip</p>
            <p class="item">24 oz Boneless Ribeye</p>
            <p class="item">36 oz Bone in Rib Eye</p>
            <p class="item">Berkshire Pork Chop</p>
          </div>
          <div class="section">
            <h2>SAUCES</h2>
            <p class="item">Cabernet Demi Glaz</p>
            <p class="item">Gorganzola Brulle Cream</p>
            <p class="item">Truffled Wild Mushroom Ragu</p>
            <p class="item">Horseradish Cream</p>
            <p class="item">House Steak Sauce</p>
          </div>
          <div class="section">
            <h2>SIDES</h2>
            <p class="item">Mashed Idaho Potatoes</p>
            <p class="item">Bacon, Sweet Corn, Caramelized Vidalia Onion fingerling potatoes</p>
            <p class="item">Roasted Peanut Potatoes</p>
            <p class="item">Creamed Spinach</p>
            <p class="item">Sautéed Spinach</p>
            <p class="item">Grilled Asparagus</p>
            <p class="item">French Beans</p>
            <p class="item">Israeli Cous Cous</p>
            <p class="item">Sweet Potato Steak Fries</p>
            <p class="item">Corn Skillet</p>
          </div>
          <div class="section">
            <h2>DESSERTS</h2>
            <p class="item">T.B.D. - separate menu</p>
          </div>
        </div>
      </div>
    </div>
  </section>

</main>
</body>
</html>
```